Business Card for Hollin Ledger - A cannabis publication for executives.

I'd like some business cards for Hollin Ledger. The logo is done (great job!) and I need a card design I will use with PELT. I made it a short project to allow time for printing before an event. These will be standard sized cards (final artwork size 3.66" x 2.16" at 300dpi) with a final card size of 3.5" x 2.0". (See PELT.example if you need more info.) I might try rounded corners but am not sure yet. I think the design will work okay with rounded.

Hollin Ledger will be a bi-weekly publication for the cannabis industry. It is targeted to investors and industry executives, not consumers or pot smokers. So our market is more B2B. However I am open to creativity and making the card something people remark on.

My contact for card:

Dara Venholm
Founder/CEO
dara@hollinledger.example

2746 Marrow Lane
Boston MA 02391
(617)555-0193

Target Market(s)

Executives, Industry people and investors in the Cannabis sector.

Contact Information for Business Card

PELT does do double sided and the second side can be the same or different images. Only one side is required but use of the second side would be a bonus.

Font styles to use
Serif
Sans Serif
Decorative

Colors

Designer to choose colors to be used in the design.

Requirements
Must have
• Logo, contact info
Nice to have
• Style and design to make the card stand out in a crowd.

```html
<!DOCTYPE html>
<html lang="en">
<head>
<meta charset="utf-8">
<title>Hollin Ledger – Business Card</title>
<link rel="stylesheet" href="https://fonts.googleapis.com/css2?family=Arimo:wght@400;700&display=swap">
<style>
  :root {
    --backdrop: #3a3431;
    --card: #151617;
    --brand-blue: #1f7fc6;
    --brand-green: #6f9c2e;
    --text-light: #ececec;
    --text-muted: #8e9092;
    --divider: #6c6e70;
  }
  * { margin: 0; padding: 0; box-sizing: border-box; }
  html, body {
    width: 1200px;
    height: 864px;
    overflow: hidden;
    background: var(--backdrop);
    font-family: "Arimo", Arial, sans-serif;
  }
  .sheet {
    width: 1200px;
    height: 864px;
    display: flex;
    flex-direction: column;
    align-items: center;
    justify-content: center;
    gap: 40px;
  }
  .card {
    width: 640px;
    height: 366px;
    background: var(--card);
    position: relative;
    box-shadow: 0 6px 18px rgba(0,0,0,0.35);
  }

  /* Back side */
  .card-back {
    display: flex;
    flex-direction: column;
    align-items: center;
    justify-content: center;
  }
  .back-mark {
    width: 118px;
    height: 118px;
    background: var(--brand-green);
    margin-bottom: 22px;
  }
  .back-name {
    color: var(--brand-blue);
    font-size: 30px;
    font-weight: 700;
    margin-bottom: 26px;
  }
  .back-web {
    color: var(--text-muted);
    font-size: 13px;
    letter-spacing: 0.42em;
  }

  /* Front side */
  .card-front {
    display: flex;
    align-items: center;
  }
  .brand {
    width: 340px;
    display: flex;
    align-items: center;
    justify-content: flex-end;
    gap: 14px;
    padding-right: 34px;
  }
  .brand-square {
    width: 46px;
    height: 46px;
    background: var(--brand-green);
    flex-shrink: 0;
  }
  .brand-name {
    color: var(--brand-blue);
    font-size: 34px;
    font-weight: 700;
    white-space: nowrap;
  }
  .divider {
    width: 1px;
    height: 190px;
    background: linear-gradient(to bottom, transparent, var(--divider) 20%, var(--divider) 80%, transparent);
  }
  .contact {
    padding-left: 26px;
    color: var(--text-light);
    font-size: 15px;
    line-height: 1.35;
  }
  .contact-name {
    color: var(--brand-blue);
    font-size: 20px;
    font-weight: 700;
  }
  .contact-title {
    color: var(--brand-green);
    font-size: 16px;
    margin-bottom: 6px;
  }
  .contact-address { margin-bottom: 8px; }
  .contact-line {
    display: flex;
    align-items: center;
    gap: 8px;
    margin-top: 3px;
  }
  .contact-line svg {
    width: 14px;
    height: 14px;
    flex-shrink: 0;
  }
</style>
</head>
<body>
<main class="sheet">
  <section class="card card-back" aria-label="Card back">
    <div class="back-mark"></div>
    <div class="back-name">Hollin Ledger</div>
    <div class="back-web">www.hollinledger.example</div>
  </section>

  <section class="card card-front" aria-label="Card front">
    <div class="brand">
      <div class="brand-square"></div>
      <div class="brand-name">Hollin Ledger</div>
    </div>
    <div class="divider"></div>
    <div class="contact">
      <div class="contact-name">Dara Venholm</div>
      <div class="contact-title">Founder/CEO</div>
      <div class="contact-address">2746 Marrow Lane<br>Boston MA 02391</div>
      <div class="contact-line">
        <svg viewBox="0 0 16 16" aria-hidden="true"><path fill="var(--brand-blue)" d="M3.5 1.5l2.5 0 1 3.5-1.6 1.1c.8 1.7 2 2.9 3.6 3.7L10.1 8.2l3.5 1v2.6c0 .9-.8 1.7-1.7 1.6C6.5 13 2.9 9.4 2.5 4.1 2.4 3 3 1.5 3.5 1.5z"/></svg>
        <span>(617)555-0193</span>
      </div>
      <div class="contact-line">
        <svg viewBox="0 0 16 16" aria-hidden="true"><rect x="1" y="3" width="14" height="10" fill="var(--brand-blue)"/><path d="M1 3.5l7 5 7-5" fill="none" stroke="var(--card)" stroke-width="1.3"/></svg>
        <span>dara@hollinledger.example</span>
      </div>
      <div class="contact-line">
        <svg viewBox="0 0 16 16" aria-hidden="true"><circle cx="8" cy="8" r="7" fill="var(--brand-blue)"/><path d="M1 8h14M8 1c-2.5 2.5-2.5 11.5 0 14M8 1c2.5 2.5 2.5 11.5 0 14" fill="none" stroke="var(--card)" stroke-width="1"/></svg>
        <span>www.hollinledger.example</span>
      </div>
    </div>
  </section>
</main>
</body>
</html>
```